Corporate WordPress Site for Global IT Staffing Firm

We are looking for a corporate web presence for our company, Corvane, that is an IT Staffing and Recruiting firm based in Silicon Valley. We want the site to convey strength, confidence and trust in our F500 global customers and be appealing to prospective job seekers looking for their next employment.
I've attached the logo scheme to you. I can provide content within the next few days as well as links to our Social, FB pages. I also have wallpaper images selected from Halden Photos for a scrolling banner. Eventually we'll post job openings with search capabilities from a third party VMS SaaS company called Tidewick.
Target Market(s)
Global 1000 companies who purchase staffing from our firm AND prospective job seekers looking for work.
Industry/Entity Type
It Company
Number of Pages Required
3 page
Requirements
Must have
- Modern, parallax design for corporate image. May need links and integration to third party systems in a few months.
- Want each of the images via slider or images to convey:
- Attention to Detail
- Taking the Time to Find the Right Candidates
- Old Fashioned Hard Work
- Assembling the Right Teams
- Built to Scale
Nice to have
- Sliders. Counters. Links to social media pages. Background information. Bio pages. Reference customers.
- Examples of sites we like.
- https://www.plavio.com/
- http://www.fennixadgroup.com/
- http://www.qorvatech.com/

```html
<!DOCTYPE html>
<html lang="en">
<head>
<meta charset="utf-8">
<title>Corvane IT Solutions</title>
<link href="https://fonts.googleapis.com/css2?family=Roboto+Condensed:wght@400;700&family=Open+Sans:ital,wght@0,400;0,600;1,400&display=swap" rel="stylesheet">
<style>
:root{
  --brand:#4a5889;
  --brand-dark:#3a4675;
  --brand-btn:#46548a;
  --ink:#222428;
  --muted:#6b6f78;
  --white:#ffffff;
  --light:#f5f5f6;
  --footer:#f1f1f2;
  --rule:#e2e3e6;
}
*{box-sizing:border-box;margin:0;padding:0}
html,body{width:1200px;height:2908px;overflow:hidden}
body{position:relative;background:var(--white);font-family:"Open Sans",Arial,sans-serif;color:var(--ink)}
.abs{position:absolute}
.heading{font-family:"Roboto Condensed","Arial Narrow",sans-serif;font-weight:700;text-transform:uppercase;text-align:center;font-size:24px;color:var(--ink);letter-spacing:.2px}
.heading .accent{color:var(--brand)}
.lead{text-align:center;font-size:16px;color:#444}
.btn{display:flex;align-items:center;justify-content:center;background:linear-gradient(#56659a,var(--brand-dark));color:var(--white);font-size:13px;box-shadow:0 2px 4px rgba(0,0,0,.35);border-radius:2px}

/* header */
.top-rule{left:0;top:0;width:1200px;height:4px;background:var(--brand)}
.site-header{left:0;top:4px;width:1200px;height:114px;background:var(--white)}
.logo{left:100px;top:30px;display:flex;align-items:center;gap:10px}
.logo-dot{width:46px;height:46px;border-radius:50%;background:var(--brand)}
.logo-name{font-family:"Roboto Condensed",sans-serif;font-weight:700;font-size:38px;color:var(--brand);line-height:1}
.logo-sub{left:158px;top:76px;font-size:9px;letter-spacing:1px;color:var(--brand)}
.main-nav{top:54px;left:0;width:1200px;font-family:Arial,sans-serif;font-size:14px;color:#222}
.main-nav span{position:absolute}
.main-nav .current{color:var(--brand)}
.nav-underline{left:488px;top:76px;width:62px;height:6px}

/* hero */
.hero{left:0;top:118px;width:1200px;height:514px;background:linear-gradient(120deg,#6f7986 0%,#9aa2ab 35%,#7b848e 60%,#5e6672 100%)}
.hero-title{left:0;top:282px;width:1200px;text-align:center;font-family:"Roboto Condensed",sans-serif;font-weight:700;font-size:38px;color:var(--white)}
.hero-text{left:300px;top:336px;width:600px;text-align:center;color:var(--white);font-size:14px;line-height:31px}
.hero-btn{left:481px;top:404px;width:239px;height:48px;font-weight:600;font-size:14px}
.hero-arrow{top:346px;width:22px;height:54px}

/* welcome */
.welcome{left:0;top:632px;width:1200px;height:311px;background:var(--white)}
.feature{top:780px;width:320px}
.feature-icon{position:absolute;left:0;top:0;width:52px;height:52px;border-radius:50%;background:var(--brand);display:flex;align-items:center;justify-content:center}
.feature h3{position:absolute;left:76px;top:2px;font-weight:400;font-size:16px;color:#333;white-space:nowrap}
.feature p{position:absolute;left:76px;top:30px;width:238px;font-size:11.5px;line-height:22px;color:var(--muted)}
.scroll-cue{width:42px;height:42px;border-radius:50%;background:var(--white);left:579px;box-shadow:0 1px 3px rgba(0,0,0,.25);display:flex;align-items:center;justify-content:center;z-index:2}

/* customers band */
.customers{left:0;top:943px;width:1200px;height:423px;background:radial-gradient(ellipse at 50% 40%,#4c4a46 0%,#2d2c2a 55%,#1b1b1b 100%)}
.on-dark{color:var(--white)}
.band-text{left:170px;top:1114px;width:860px;text-align:center;font-size:12.5px;line-height:23px;color:var(--white)}

/* processes */
.process-photo{left:100px;top:1494px;width:478px;height:284px;background:linear-gradient(135deg,#e9eaec 0%,#cfd2d6 55%,#aeb2b8 100%);box-shadow:0 6px 10px rgba(0,0,0,.2)}
.process-kicker{left:604px;top:1486px;font-family:"Roboto Condensed",sans-serif;font-weight:700;font-size:21px;color:var(--brand)}
.process-title{left:604px;top:1520px;font-size:29px;font-weight:400;color:#444}
.process-copy{left:606px;top:1572px;width:420px;font-size:11.5px;line-height:23px;color:var(--muted)}
.process-copy p+p{margin-top:8px}

/* testimonials */
.testimonials{left:0;top:1832px;width:1200px;height:424px;background:radial-gradient(ellipse at 50% 50%,#4a4140 0%,#2a2524 55%,#141414 100%)}
.quote-text{left:270px;top:1982px;width:700px;text-align:center;color:var(--white);font-size:12.5px;line-height:24px}
.quote-mark{font-family:Georgia,serif;font-size:34px;color:var(--white);line-height:1}
.avatar{left:474px;top:2100px;width:84px;height:84px;border-radius:50%;background:radial-gradient(circle at 50% 40%,#c9b7a6,#7b6d62);border:4px solid var(--white)}
.author-name{left:580px;top:2118px;font-size:13px;color:var(--white)}
.author-role{left:580px;top:2142px;font-size:13px;font-style:italic;color:var(--white)}

/* partners */
.partners{left:0;top:2256px;width:1200px;height:352px;background:var(--white)}
.partner{width:176px;height:98px;border:5px solid #eeeeef;background:var(--white);display:flex;align-items:center;justify-content:center}
.partner i{display:block;width:110px;height:26px;border-radius:13px;background:#d4d6da}

/* footer */
.site-footer{left:0;top:2608px;width:1200px;height:252px;background:var(--footer)}
.footer-col{top:2636px}
.footer-col h4{font-family:"Roboto Condensed",sans-serif;font-weight:700;font-size:16px;text-transform:uppercase;color:var(--ink);margin-bottom:14px}
.footer-col p{font-size:11.5px;line-height:22px;color:#333}
.tweet{display:flex;gap:14px;font-size:11.5px;line-height:22px;color:#333;padding-bottom:12px}
.tweet+.tweet{border-top:1px solid #cfd0d4;padding-top:12px}
.tweet-dot{flex:none;width:12px;height:12px;border-radius:50%;background:#444;margin-top:5px}
.contact-line{display:flex;align-items:center;gap:12px;font-size:11.5px;color:#333;height:28px}
.newsletter{display:flex;margin-top:16px}
.newsletter span{width:168px;height:34px;background:#e4e5e8;border:1px solid #d6d7db;font-style:italic;font-size:11px;color:#8a8d94;display:flex;align-items:center;padding-left:10px}
.newsletter b{width:70px;height:34px;background:var(--brand-dark);color:var(--white);font-weight:400;font-size:11px;display:flex;align-items:center;justify-content:center}

.bottom-bar{left:0;top:2860px;width:1200px;height:48px;background:var(--brand)}
.social{left:100px;top:2872px;display:flex;gap:6px}
.social i{width:22px;height:22px;border-radius:50%;border:1.5px solid var(--white)}
.copyright{left:838px;top:2877px;font-size:11px;color:#e7e9f2}
.page-tag{left:1146px;top:2877px;font-size:11px;font-weight:600;color:var(--white)}
</style>
</head>
<body>

<div class="abs top-rule"></div>
<header class="abs site-header"></header>
<div class="abs logo"><span class="logo-dot"></span><span class="logo-name">CORVANE</span></div>
<div class="abs logo-sub">IT SOLUTIONS</div>
<nav class="abs main-nav">
  <span class="current" style="left:496px">About us</span>
  <span style="left:603px">Candidate</span>
  <span style="left:718px">Hardwork</span>
  <span style="left:830px">Team</span>
  <span style="left:920px">Built to Scale</span>
  <span style="left:1052px">Contact</span>
</nav>
<svg class="abs nav-underline" viewBox="0 0 62 6"><path d="M1 5 Q31 -1 61 5" stroke="#4a5889" stroke-width="2" fill="none"/></svg>

<section class="abs hero" role="img" aria-label="Photo of a team joining jigsaw puzzle pieces over a table"></section>
<svg class="abs hero-arrow" style="left:46px" viewBox="0 0 22 54"><path d="M20 2 L3 27 L20 52" stroke="#fff" stroke-width="2" fill="none"/></svg>
<svg class="abs hero-arrow" style="left:1144px" viewBox="0 0 22 54"><path d="M2 2 L19 27 L2 52" stroke="#fff" stroke-width="2" fill="none"/></svg>
<h1 class="abs hero-title">ATTENTION TO DETAIL</h1>
<p class="abs hero-text">Sed ut perspiciatis unde omnis iste natus error sit voluptatem accusantium do-<br>loremque laudantium, totam rem aperiam, eaque ipsa quae ab</p>
<div class="abs btn hero-btn">VIEW MORE INFORMATION</div>

<section class="abs welcome"></section>
<h2 class="abs heading" style="left:0;top:670px;width:1200px">WELCOME TO <span class="accent">CORVANE IT SOLUTIONS</span></h2>
<p class="abs lead" style="left:0;top:714px;width:1200px">Lorem Ipsum is simply dummy text of the printing and typesetting industry.</p>

<div class="abs feature" style="left:100px">
  <div class="feature-icon"><svg width="20" height="20" viewBox="0 0 20 20"><rect x="3" y="2" width="14" height="16" rx="2" fill="#fff"/><rect x="6" y="5" width="8" height="2" fill="#4a5889"/></svg></div>
  <h3>Finibus Bonorum et</h3>
  <p>Lorem Ipsum is simply dummy text of the printing and typesetting industry. Lorem Ipsum has been the industry's...</p>
</div>
<div class="abs feature" style="left:450px">
  <div class="feature-icon"><svg width="20" height="20" viewBox="0 0 20 20"><rect x="2" y="3" width="16" height="14" rx="2" fill="none" stroke="#fff" stroke-width="2"/><rect x="6" y="7" width="5" height="6" fill="#fff"/></svg></div>
  <h3>Et accusamus et iusto</h3>
  <p>Lorem Ipsum is simply dummy text of the printing and typesetting industry. Lorem Ipsum has been the industry's...</p>
</div>
<div class="abs feature" style="left:795px">
  <div class="feature-icon"><svg width="22" height="22" viewBox="0 0 22 22"><circle cx="8" cy="8" r="5" fill="none" stroke="#fff" stroke-width="2.5"/><circle cx="15.5" cy="15.5" r="3.5" fill="none" stroke="#fff" stroke-width="2"/></svg></div>
  <h3>Dignissimos ducimus qui</h3>
  <p>Lorem Ipsum is simply dummy text of the printing and typesetting industry. Lorem Ipsum has been the industry's...</p>
</div>
<div class="abs scroll-cue" style="top:921px"><svg width="12" height="8" viewBox="0 0 12 8"><path d="M1 1 L6 6 L11 1" stroke="#888" stroke-width="1.5" fill="none"/></svg></div>

<section class="abs customers" role="img" aria-label="Aerial photo of a crowd of people holding hands in a circle"></section>
<h2 class="abs heading on-dark" style="left:0;top:1066px;width:1200px">DO YOU KNOW WHAT YOUR CUSTOMERS ARE DOING</h2>
<p class="abs band-text">Lorem Ipsum is simply dummy text of the printing and typesetting industry. Lorem Ipsum has been the industry's standard dummy text ever since the 1500s, when an unknown printer took a galley of type and scrambled it to make a type specimen book. It has survived not only five centuries, but also the leap into electronic typesetting, remaining essentially unchanged.</p>
<div class="abs btn" style="left:492px;top:1210px;width:216px;height:43px">Click here for more info</div>

<h2 class="abs heading" style="left:0;top:1404px;width:1200px">OUR PROCESSES <span class="accent">DELIVER RESULTS</span></h2>
<p class="abs lead" style="left:0;top:1442px;width:1200px">Lorem Ipsum is simply dummy text of the printing and typesetting industry.</p>
<div class="abs process-photo" role="img" aria-label="Illustration of business people assembling large white puzzle blocks"></div>
<h3 class="abs process-kicker">AT VERO EOS ET ACCUSAMUS IUSTO</h3>
<p class="abs process-title">Sed ut perspiciatis unde omnis.</p>
<div class="abs process-copy">
  <p>I must explain to you how all this mistaken idea of denouncing pleasure and praising pain was born and I will give you a complete account of the system, and expound the actual teachings of the great explorer of the truth, the master-builder of human happiness.</p>
  <p>occur in which toil and pain can procure him some great pleasure. To take a trivial example, which of us ever undertakes</p>
</div>
<div class="abs btn" style="left:606px;top:1735px;width:218px;height:43px">Click here for more info</div>
<div class="abs scroll-cue" style="top:1811px"><svg width="12" height="8" viewBox="0 0 12 8"><path d="M1 1 L6 6 L11 1" stroke="#888" stroke-width="1.5" fill="none"/></svg></div>

<section class="abs testimonials" role="img" aria-label="Dark photo of stacked hands in a team huddle"></section>
<h2 class="abs heading on-dark" style="left:0;top:1914px;width:1200px">TESTIMONIALS</h2>
<span class="abs quote-mark" style="left:238px;top:1972px">&ldquo;</span>
<p class="abs quote-text">Lorem Ipsum is simply dummy text of the printing and typesetting industry. Lorem Ipsum has been the industry's standard dummy text ever since the 1500s, when an unknown printer took a galley of type and scrambled it to make a type specimen book. It has survived not only five centuries, but also the leap into electronic typesetting</p>
<span class="abs quote-mark" style="left:950px;top:2068px">&rdquo;</span>
<div class="abs avatar" role="img" aria-label="Portrait photo of the client"></div>
<div class="abs author-name">Elias Marlow</div>
<div class="abs author-role">Assistant manager</div>

<section class="abs partners"></section>
<h2 class="abs heading" style="left:0;top:2296px;width:1200px">OUR <span class="accent">PARTNERS</span></h2>
<div class="abs partner" style="left:100px;top:2346px"><i></i></div>
<div class="abs partner" style="left:306px;top:2346px"><i></i></div>
<div class="abs partner" style="left:510px;top:2346px"><i></i></div>
<div class="abs partner" style="left:718px;top:2346px"><i></i></div>
<div class="abs partner" style="left:923px;top:2346px"><i></i></div>
<div class="abs partner" style="left:100px;top:2474px"><i></i></div>
<div class="abs partner" style="left:306px;top:2474px"><i></i></div>
<div class="abs partner" style="left:510px;top:2474px"><i></i></div>
<div class="abs partner" style="left:718px;top:2474px"><i></i></div>
<div class="abs partner" style="left:923px;top:2474px"><i></i></div>

<footer class="abs site-footer"></footer>
<div class="abs footer-col" style="left:100px;width:210px">
  <h4>About us</h4>
  <p>Lorem Ipsum is simply dummy text of the printing and typesetting industry. Lorem Ipsum has been the industry's standard dummy text ever since the 1500s, when an printer</p>
</div>
<div class="abs footer-col" style="left:374px;width:252px">
  <h4>Social feed</h4>
  <div class="tweet"><span class="tweet-dot"></span><span>The Harlow Quinby Daily is out!<br>pagewire.io/asin about 23 hours ago</span></div>
  <div class="tweet"><span class="tweet-dot"></span><span>The Harlow Quinby Daily is out!<br>pagewire.io/asin Stories via @marenholt<br>about a day ago</span></div>
</div>
<div class="abs footer-col" style="left:654px;width:180px">
  <h4>Contact</h4>
  <p>CORVANE IT Solutions.<br>120 Alder Row, Brenmoor<br>AZ USA, 85990</p>
  <div style="margin-top:6px">
    <div class="contact-line"><svg width="10" height="14" viewBox="0 0 10 14"><rect x="1" y="1" width="8" height="12" rx="1.5" fill="none" stroke="#333" stroke-width="1.5"/></svg>555 210 0731</div>
    <div class="contact-line"><svg width="12" height="12" viewBox="0 0 12 12"><rect x="1" y="4" width="10" height="6" fill="#333"/><rect x="3" y="1" width="6" height="3" fill="#333"/></svg>555 210 0732</div>
    <div class="contact-line"><svg width="12" height="9" viewBox="0 0 12 9"><rect x="0.5" y="0.5" width="11" height="8" fill="none" stroke="#333"/><path d="M1 1 L6 5 L11 1" stroke="#333" fill="none"/></svg>info@corvane-it.com</div>
  </div>
</div>
<div class="abs footer-col" style="left:861px;width:240px">
  <h4>News letter</h4>
  <p>Lorem Ipsum is simply dummy text of the printing and typesetting industry. Lorem Ipsum has been the industry's standard</p>
  <div class="newsletter"><span>Enter your email address...</span><b>SUBMIT</b></div>
</div>

<div class="abs bottom-bar"></div>
<div class="abs social"><i></i><i></i><i></i><i></i><i></i></div>
<div class="abs copyright">Copyright &copy; CORVANE IT Solutions.All rights reserved.</div>
<div class="abs page-tag">C12</div>

</body>
</html>
```